Food fans website needs a desktop homepage design

We need a desktop homepage design for TableHop.co.uk, a website to help you to find the best restaurants in each main city of Europe, with initial focus on London. It is not a directory with thousands of restaurants and reviews, else lists of top 20 restaurants for each area of the city. Food fans from all around the city will be able to keep an itinerary of where they eat, showing them later funny stats like "this month you really went for pizzas, don't you?". Keep it funny but professional.

A bit of branding has been done but this project give you total freedom to design the homepage of the site. The design must be a mix between minimal, flat and clean layout. The main idea is to keep it simple, easy to use and showing just the necessary elements.

For the font and colour scheme, we would like to use a thin but energetic font using the #E1393A colour as starting point even if you have freedom to slightly modify it. Blacks, greys and whites can be the secondary colours but we are open to introduce another main colour to the site like green, orange or yellow.

A simple wireframe has been attached to help you but the main elements that the page requires are the next:
- Panoramic fancy image in the header to contain the logo and the search form (the fields of the form are specified on the wireframe) and maybe some animated text to fill the right gap.
- List of results (10 results per page) showing the main info for each restaurant: name, thumbnail, location (zone, area), category, price, description, rating (no with stars please) and whatever you want to add that makes sense.
- Right hand sidebar with 3 widgets: Categories, Location and prices.

You can get the icons from glyphbarn.net.

We are open to have some text-shadows, rounded corners, box-shadows but trying to keep it minimal, flat and clean as much as possible. The main attractive of the site are the food/restaurant images.

Target Market(s)

22 - 45 food fans lovers from the city. busy people that want to disconnect and relax through the food. The don't mind to pay for quality and new experiences. Up to meet new places around them.

Industry/Entity Type

Restaurant

Requirements
Must have
• Panoramic image in the header, restaurants search form as per wireframe, list results with pagination, right hand sidebar with the widgets mention above and a nice footer with extra elements like "latest restaurants, latest tweets, etc.."
Nice to have
• This site will only be supported by the latest browsers so the idea is to have nice CSS3 transitions all around. Have that in mind at the time to design it even if you cannot show it on the design.
Should not have
• Busy backgrounds and unnecessary images that would slow down the page load.

```html
<!DOCTYPE html>
<html lang="en">
<head>
<meta charset="utf-8">
<title>TableHop in London – Best Restaurants</title>
<link rel="stylesheet" href="https://fonts.googleapis.com/css2?family=Raleway:wght@300;400;500;600;700&family=Roboto+Slab:wght@400;700&family=Lora:ital@1&display=swap">
<style>
:root{
  --red:#e1393a;
  --red-dark:#c22a2b;
  --green:#7cb518;
  --green-dark:#5f9410;
  --yellow:#f5d90f;
  --cream:#f7f3e5;
  --ink:#222222;
  --grey:#8a8a8a;
  --grey-light:#f1f1f1;
  --panel:#232323;
  --panel-line:#3c3c3c;
  --sky:#13a5e6;
  --footer:#1e1e1e;
  --footer-base:#161616;
  --white:#ffffff;
}
*{box-sizing:border-box;margin:0;padding:0}
html,body{width:1200px;height:2387px;overflow:hidden}
body{position:relative;background:var(--cream);font-family:"Raleway",sans-serif;color:var(--ink)}
.abs{position:absolute}
svg.ico{width:12px;height:12px;fill:currentColor;flex:none}

/* Hero */
.hero{left:0;top:0;width:1200px;height:433px;background:radial-gradient(ellipse at 60% 40%,#8a6a72 0%,#4f3640 35%,#2a1b22 70%,#1a1115 100%)}
.hero-figure{left:207px;top:40px;width:225px;height:286px;border-radius:110px 110px 0 0;background:linear-gradient(180deg,#b76a4a 0%,#d9b7a3 45%,#e9e2dc 100%);opacity:.9}
.brand{left:442px;top:0;width:331px;height:64px;background:var(--white);display:flex;align-items:center;justify-content:center;gap:10px;box-shadow:0 2px 6px rgba(0,0,0,.3)}
.brand-dot{width:14px;height:14px;border-radius:50%;background:var(--red)}
.brand-name{font-family:"Roboto Slab",serif;font-weight:700;font-size:22px;color:var(--red)}
.topnav{left:820px;top:21px;display:flex;align-items:center;gap:14px;font-size:11px;color:var(--white)}
.city-select{width:75px;height:22px;background:#111;color:var(--white);font-size:10px;display:flex;align-items:center;justify-content:space-between;padding:0 8px}
.city-select::after{content:"";border:4px solid transparent;border-top-color:var(--white);margin-top:4px}
.tagline{left:525px;top:143px;width:458px;height:80px;background:rgba(20,14,16,.75);color:var(--white);font-family:"Roboto Slab",serif;font-weight:700;font-size:20px;line-height:28px;padding:11px 16px;text-shadow:0 1px 2px rgba(0,0,0,.6)}
.tagline::before{content:"";position:absolute;left:-14px;top:22px;border:8px solid transparent;border-right:7px solid rgba(20,14,16,.75)}
.search-tab{left:239px;top:299px;width:114px;height:26px;background:var(--white);font-family:"Roboto Slab",serif;font-weight:700;font-size:14px;text-align:center;line-height:28px}
.search{left:215px;top:325px;width:772px;height:79px;background:var(--white);box-shadow:0 2px 8px rgba(0,0,0,.3)}
.field{position:absolute;top:22px}
.field label{display:block;font-size:11px;color:#444;margin-bottom:6px}
.field .input{height:30px;border:1px solid #e3e3e3;background:#fafafa;display:flex;align-items:center;font-size:10px;font-style:italic;color:#aaa}
.field .input .cap{width:28px;height:100%;border-right:1px solid #e3e3e3;display:flex;align-items:center;justify-content:center;color:#bbb}
.field .input span{padding-left:10px}
.search-btn{position:absolute;left:652px;top:35px;width:104px;height:30px;background:linear-gradient(var(--green),var(--green-dark));color:var(--white);font-family:"Roboto Slab",serif;font-weight:700;font-size:13px;text-align:center;line-height:30px;border-radius:2px}

/* Listing */
.list-title{left:213px;top:456px;font-size:20px;font-weight:500}
.list-tabs{left:536px;top:466px;font-size:10px;display:flex;gap:12px}
.card{left:215px;width:481px;height:139px;background:var(--white);box-shadow:0 1px 3px rgba(0,0,0,.12);display:flex}
.card-photo{width:172px;height:139px;flex:none}
.card-body{position:relative;flex:1}
.card-name{position:absolute;left:16px;top:12px;font-size:13px;font-weight:600;display:flex;align-items:center;gap:7px}
.rating{background:var(--yellow);color:#333;font-size:7px;font-weight:600;padding:2px 4px;border-radius:2px}
.card-desc{position:absolute;left:16px;top:32px;width:285px;font-size:9px;line-height:12px;color:#9a9a9a;height:36px;overflow:hidden}
.meta{position:absolute;top:78px;display:flex;align-items:center;gap:8px;font-size:8.5px;line-height:11px;color:#444}
.meta .disc{width:24px;height:24px;border-radius:50%;background:var(--grey-light);display:flex;align-items:center;justify-content:center;color:#333}
.meta-price{left:16px}
.meta-place{left:176px}
.card-foot{position:absolute;left:0;right:0;bottom:0;height:30px;background:#f4f4f4;display:flex;align-items:center;justify-content:space-between;padding:0 12px 0 16px}
.phone{display:flex;align-items:center;gap:7px;font-weight:700;font-size:12px}
.link{display:flex;align-items:center;gap:5px;font-size:8px;color:#555}
.card.featured .card-body{background:var(--red)}
.card.featured .card-name,.card.featured .card-desc,.card.featured .meta,.card.featured .phone,.card.featured .link{color:var(--white)}
.card.featured .meta .disc{background:rgba(255,255,255,.9);color:var(--red)}
.card.featured .card-foot{background:var(--red-dark)}

.pager{left:283px;top:2045px;display:flex;align-items:center;gap:9px;font-size:9px;color:#444}
.pager .arrow{width:0;height:0;border:7px solid transparent}
.pager .prev{border-right:10px solid #222;border-left:0}
.pager .next{border-left:10px solid #222;border-right:0}
.pager .current{background:var(--red);color:var(--white);padding:2px 4px}

/* Sidebar */
.signup{left:756px;top:466px;width:231px;height:174px;background:var(--red);color:var(--white);overflow:hidden}
.signup h3{position:absolute;left:21px;top:26px;font-size:21px;font-weight:500}
.signup p{position:absolute;left:21px;top:57px;width:125px;font-size:9px;line-height:11px}
.signup-figure{position:absolute;right:0;top:48px;width:86px;height:126px;border-radius:43px 43px 0 0;background:linear-gradient(180deg,#6b3320,#c0796a 50%,#e4c3b6)}
.btn-green{position:absolute;left:21px;top:108px;width:62px;height:22px;background:var(--green);font-size:10px;font-weight:600;text-align:center;line-height:22px}
.widget{left:756px;width:231px;background:var(--panel);color:var(--white)}
.widget h4{display:flex;align-items:center;gap:8px;margin:16px 18px 0;padding-bottom:8px;border-bottom:1px solid var(--panel-line);font-size:15px;font-weight:500;letter-spacing:.3px}
.widget h4 svg{width:14px;height:14px;fill:var(--white)}
.widget ul{list-style:none;margin:10px 18px 0 22px}
.widget li{font-size:9px;color:#c9c9c9;height:26.4px;line-height:26.4px;position:relative;padding-left:13px;white-space:nowrap}
.widget li::before{content:"";position:absolute;left:0;top:12px;width:3px;height:3px;background:#888}
.feature{left:756px;top:1571px;width:231px;height:294px;background:var(--red);color:var(--white)}
.feature h4{position:absolute;left:20px;top:14px;font-size:17px;font-weight:500}
.feature-photo{position:absolute;left:22px;top:48px;width:187px;height:112px;border:4px solid var(--white);background:linear-gradient(135deg,#c9a585,#8e5a3a 55%,#3e2418)}
.feature p{position:absolute;left:22px;top:173px;width:187px;font-size:9px;line-height:11.5px}
.feature .btns{position:absolute;left:22px;top:245px;display:flex;gap:6px}
.feature .btns span{background:#111;font-size:8.5px;font-weight:600;height:20px;line-height:20px;text-align:center}

/* Footer */
.tweets{left:0;top:2098px;width:1200px;height:111px;background:var(--sky);color:var(--white)}
.tweets h5{position:absolute;left:230px;top:30px;font-size:24px;font-weight:400}
.tweets small{position:absolute;left:230px;top:62px;font-size:11px;letter-spacing:1px;text-transform:uppercase}
.tweets .brace{position:absolute;left:410px;top:22px;font-size:64px;font-weight:300;line-height:64px}
.tweets blockquote{position:absolute;left:460px;top:34px;font-family:"Lora",serif;font-style:italic;font-size:19px;line-height:26px}
.tweets .bird{position:absolute;left:850px;top:10px;width:20px;height:20px;border-radius:50%;background:var(--white)}
.footer{left:0;top:2209px;width:1200px;height:146px;background:var(--footer);color:var(--white)}
.col{position:absolute;top:34px}
.col h6{font-size:13px;font-weight:500;color:var(--red);margin-bottom:10px}
.col-latest{left:213px}
.col-latest .names{display:grid;grid-template-columns:80px 110px;font-size:9px;line-height:15px;color:#ddd;white-space:nowrap}
.col-contact{left:427px}
.contact-row{display:flex;align-items:center;gap:8px;font-size:10px;margin-bottom:9px}
.contact-row .disc{width:22px;height:22px;border-radius:50%;background:var(--white);color:#222;display:flex;align-items:center;justify-content:center}
.col-social{left:606px}
.social-row{display:flex;align-items:center;gap:8px;font-size:9px;line-height:19px}
.social-row i{width:7px;height:7px;background:var(--white)}
.col-news{left:767px}
.news-input{width:220px;height:21px;background:var(--white);color:#999;font-size:8px;line-height:21px;padding-left:8px}
.news-row{display:flex;gap:8px;margin-top:8px}
.news-btn{width:94px;height:21px;background:var(--red);font-size:9.5px;font-weight:600;text-align:center;line-height:21px}
.news-row small{font-size:7.5px;line-height:9px;color:#aaa;width:110px}
.base{left:0;top:2355px;width:1200px;height:32px;background:var(--footer-base);color:#888;font-size:8.5px;text-align:center;line-height:32px}
</style>
</head>
<body>
<svg width="0" height="0" style="position:absolute">
  <symbol id="i-pin" viewBox="0 0 24 24"><path d="M12 2a7 7 0 0 0-7 7c0 5 7 13 7 13s7-8 7-13a7 7 0 0 0-7-7zm0 9.5A2.5 2.5 0 1 1 12 6.5a2.5 2.5 0 0 1 0 5z"/></symbol>
  <symbol id="i-tag" viewBox="0 0 24 24"><path d="M2 12V3h9l11 11-9 9L2 12zm5-4.5a1.5 1.5 0 1 0 0-.01z"/></symbol>
  <symbol id="i-phone" viewBox="0 0 24 24"><path d="M6.6 10.8a15 15 0 0 0 6.6 6.6l2.2-2.2a1 1 0 0 1 1-.25 11.4 11.4 0 0 0 3.6.57 1 1 0 0 1 1 1V20a1 1 0 0 1-1 1A17 17 0 0 1 3 4a1 1 0 0 1 1-1h3.5a1 1 0 0 1 1 1c0 1.25.2 2.45.57 3.6a1 1 0 0 1-.25 1z"/></symbol>
  <symbol id="i-link" viewBox="0 0 24 24"><path d="M10 14a4 4 0 0 0 5.7 0l4-4a4 4 0 0 0-5.7-5.7l-1.5 1.5 1.4 1.4 1.5-1.5a2 2 0 0 1 2.9 2.9l-4 4a2 2 0 0 1-2.9 0zm4-4a4 4 0 0 0-5.7 0l-4 4a4 4 0 0 0 5.7 5.7l1.5-1.5-1.4-1.4-1.5 1.5a2 2 0 0 1-2.9-2.9l4-4a2 2 0 0 1 2.9 0z"/></symbol>
  <symbol id="i-mail" viewBox="0 0 24 24"><path d="M3 5h18v14H3zm2 2v.5l7 5 7-5V7l-7 5z"/></symbol>
  <symbol id="i-search" viewBox="0 0 24 24"><path d="M10 3a7 7 0 1 0 4.2 12.6l5 5 1.4-1.4-5-5A7 7 0 0 0 10 3zm0 2a5 5 0 1 1 0 10 5 5 0 0 1 0-10z"/></symbol>
</svg>

<header class="abs hero" role="img" aria-label="Blurred evening photograph of a warmly lit restaurant dining room"></header>
<div class="abs hero-figure" role="img" aria-label="Illustrated smiling food fan in glasses pointing upward"></div>
<div class="abs brand"><span class="brand-dot"></span><span class="brand-name">TableHop in London</span></div>
<nav class="abs topnav"><span>Sign up</span><span>Login</span><span class="city-select">London</span></nav>
<div class="abs tagline">Book Tables and Get FANTASTIC OFFERS at Your Favourite Restaurants FOR FREE</div>

<div class="abs search-tab">SEARCH</div>
<form class="abs search">
  <div class="field" style="left:13px;width:218px"><label>What Restaurant?</label><div class="input"><i class="cap"><svg class="ico"><use href="#i-search"/></svg></i><span>Sushi</span></div></div>
  <div class="field" style="left:235px;width:134px"><label>What kind of food?</label><div class="input"><i class="cap"><svg class="ico"><use href="#i-tag"/></svg></i><span>All</span></div></div>
  <div class="field" style="left:374px;width:135px"><label>Where?</label><div class="input"><i class="cap"><svg class="ico"><use href="#i-pin"/></svg></i><span>Everywhere</span></div></div>
  <div class="field" style="left:514px;width:134px"><label>Prices?</label><div class="input"><i class="cap"><svg class="ico"><use href="#i-tag"/></svg></i><span>All</span></div></div>
  <div class="search-btn">SEARCH</div>
</form>

<h2 class="abs list-title">Best Restaurants in London</h2>
<div class="abs list-tabs"><span>Top Search</span><span>Popular Restaurants</span></div>

<article class="abs card" style="top:501px">
  <div class="card-photo" role="img" aria-label="Brasserie interior with red leather banquettes" style="background:linear-gradient(135deg,#6e2b1f,#a45a3b 50%,#d8b28d)"></div>
  <div class="card-body">
    <h3 class="card-name">Best Brasseries <span class="rating">5/10 Ratings</span></h3>
    <p class="card-desc">Fancy brunch somewhere special? Or how about elevenses, or afternoon tea? In fact, why not make a meal of it at these open-all-day, Continental-style brasseries.</p>
    <div class="meta meta-price"><span class="disc"><svg class="ico"><use href="#i-tag"/></svg></span>Main courses £13-£37</div>
    <div class="meta meta-place"><span class="disc"><svg class="ico"><use href="#i-pin"/></svg></span>12 Lantern Row<br>London WC2E 9XX</div>
    <div class="card-foot"><span class="phone"><svg class="ico"><use href="#i-phone"/></svg>020 7946 0123</span><span class="link"><svg class="ico"><use href="#i-link"/></svg>www.brasseriemarlow.co.uk</span></div>
  </div>
</article>

<article class="abs card featured" style="top:654px">
  <div class="card-photo" role="img" aria-label="Steak and sides on a dark wooden table" style="background:linear-gradient(135deg,#3a2a22,#7a5a44 50%,#c9b8a6)"></div>
  <div class="card-body">
    <h3 class="card-name">Emberline Seven Dials <span class="rating">5/10 Ratings</span></h3>
    <p class="card-desc">The original Emberline by the market is a great bar and grill, but this newer branch is a truly sensational one. The entrance is a bit hidden, despite the busy square outside.</p>
    <div class="meta meta-price"><span class="disc"><svg class="ico"><use href="#i-tag"/></svg></span>Main courses £13-£37</div>
    <div class="meta meta-place"><span class="disc"><svg class="ico"><use href="#i-pin"/></svg></span>12 Lantern Row<br>London WC2E 9XX</div>
    <div class="card-foot"><span class="phone"><svg class="ico"><use href="#i-phone"/></svg>020 7946 0123</span><span class="link"><svg class="ico"><use href="#i-link"/></svg>www.brasseriemarlow.co.uk</span></div>
  </div>
</article>

<article class="abs card" style="top:807px">
  <div class="card-photo" role="img" aria-label="Dim sum dishes on a dark lacquered table" style="background:linear-gradient(135deg,#2d231e,#7d5c3a 55%,#c08e4e)"></div>
  <div class="card-body">
    <h3 class="card-name">Jadehouse <span class="rating">5/10 Ratings</span></h3>
    <p class="card-desc">The original branch founded (then sold) by its chef still remains an iconic venue for smart lunchtime dim sum or an evening cocktail or two.</p>
    <div class="meta meta-price"><span class="disc"><svg class="ico"><use href="#i-tag"/></svg></span>Main courses £13-£37</div>
    <div class="meta meta-place"><span class="disc"><svg class="ico"><use href="#i-pin"/></svg></span>12 Lantern Row<br>London WC2E 9XX</div>
    <div class="card-foot"><span class="phone"><svg class="ico"><use href="#i-phone"/></svg>020 7946 0123</span><span class="link"><svg class="ico"><use href="#i-link"/></svg>www.brasseriemarlow.co.uk</span></div>
  </div>
</article>

<article class="abs card" style="top:960px">
  <div class="card-photo" role="img" aria-label="Burger with a basket of fries" style="background:linear-gradient(135deg,#d9a441,#b5772d 50%,#e9dcc4)"></div>
  <div class="card-body">
    <h3 class="card-name">Bar Marceau <span class="rating">5/10 Ratings</span></h3>
    <p class="card-desc">It pains us to rate a US import so highly, but this branch of the original in New York has won us over. It is a seamless dining experience, with faultless service.</p>
    <div class="meta meta-price"><span class="disc"><svg class="ico"><use href="#i-tag"/></svg></span>Main courses £13-£37</div>
    <div class="meta meta-place"><span class="disc"><svg class="ico"><use href="#i-pin"/></svg></span>12 Lantern Row<br>London WC2E 9XX</div>
    <div class="card-foot"><span class="phone"><svg class="ico"><use href="#i-phone"/></svg>020 7946 0123</span><span class="link"><svg class="ico"><use href="#i-link"/></svg>www.brasseriemarlow.co.uk</span></div>
  </div>
</article>

<article class="abs card" style="top:1113px">
  <div class="card-photo" role="img" aria-label="Gastropub plate with bread and greens" style="background:linear-gradient(135deg,#e7e1d6,#9c8a6c 50%,#5a6b3a)"></div>
  <div class="card-body">
    <h3 class="card-name">Fox &amp; Furrow <span class="rating">5/10 Ratings</span></h3>
    <p class="card-desc">Locals are spoiled with this gastropub on their doorstep, though good luck to them on a weekend. The food is certainly worth travelling for, and people do.</p>
    <div class="meta meta-price"><span class="disc"><svg class="ico"><use href="#i-tag"/></svg></span>Main courses £13-£37</div>
    <div class="meta meta-place"><span class="disc"><svg class="ico"><use href="#i-pin"/></svg></span>12 Lantern Row<br>London WC2E 9XX</div>
    <div class="card-foot"><span class="phone"><svg class="ico"><use href="#i-phone"/></svg>020 7946 0123</span><span class="link"><svg class="ico"><use href="#i-link"/></svg>www.brasseriemarlow.co.uk</span></div>
  </div>
</article>

<article class="abs card" style="top:1266px">
  <div class="card-photo" role="img" aria-label="White plated dish on a pale table" style="background:linear-gradient(135deg,#f2f2f0,#cfcfcb 55%,#8f8f8a)"></div>
  <div class="card-body">
    <h3 class="card-name">Verdance <span class="rating">5/10 Ratings</span></h3>
    <p class="card-desc">The chef and his eponymous restaurant were the runaway success of 2012. Within weeks of opening, the phones were ringing non-stop.</p>
    <div class="meta meta-price"><span class="disc"><svg class="ico"><use href="#i-tag"/></svg></span>Main courses £13-£37</div>
    <div class="meta meta-place"><span class="disc"><svg class="ico"><use href="#i-pin"/></svg></span>41 Copper Lane,<br>W1T 4ZZ</div>
    <div class="card-foot"><span class="phone"><svg class="ico"><use href="#i-phone"/></svg>020 7946 0123</span><span class="link"><svg class="ico"><use href="#i-link"/></svg>www.brasseriemarlow.co.uk</span></div>
  </div>
</article>

<article class="abs card" style="top:1419px">
  <div class="card-photo" role="img" aria-label="Italian salad on a white plate" style="background:linear-gradient(135deg,#f0ece4,#c8a58a 50%,#9b4c3d)"></div>
  <div class="card-body">
    <h3 class="card-name">Bocca di Volpe <span class="rating">5/10 Ratings</span></h3>
    <p class="card-desc">It's not so much a lone wolf; this Soho trattoria has garnered quite a following. The chef is a skilled hand when it comes to executing treasured dishes of Italy.</p>
    <div class="meta meta-price"><span class="disc"><svg class="ico"><use href="#i-tag"/></svg></span>Main courses £13-£37</div>
    <div class="meta meta-place"><span class="disc"><svg class="ico"><use href="#i-pin"/></svg></span>88 Quayside Street,<br>SE1 5QQ</div>
    <div class="card-foot"><span class="phone"><svg class="ico"><use href="#i-phone"/></svg>020 7946 0123</span><span class="link"><svg class="ico"><use href="#i-link"/></svg>www.brasseriemarlow.co.uk</span></div>
  </div>
</article>

<article class="abs card" style="top:1572px">
  <div class="card-photo" role="img" aria-label="Row of small Japanese bites on a wooden board" style="background:linear-gradient(135deg,#f4efe6,#c2873f 50%,#b4302a)"></div>
  <div class="card-body">
    <h3 class="card-name">Kumo Table <span class="rating">5/10 Ratings</span></h3>
    <p class="card-desc">This tiny Japanese restaurant, set in a beautiful Georgian townhouse, is a place we recommend for a treat. The contemporary take on Japanese cuisine means small plates.</p>
    <div class="meta meta-price"><span class="disc"><svg class="ico"><use href="#i-tag"/></svg></span>Main courses £13-£37</div>
    <div class="meta meta-place"><span class="disc"><svg class="ico"><use href="#i-pin"/></svg></span>41 Copper Lane,<br>W1T 4ZZ</div>
    <div class="card-foot"><span class="phone"><svg class="ico"><use href="#i-phone"/></svg>020 7946 0123</span><span class="link"><svg class="ico"><use href="#i-link"/></svg>www.brasseriemarlow.co.uk</span></div>
  </div>
</article>

<article class="abs card" style="top:1725px">
  <div class="card-photo" role="img" aria-label="Bowls of udon noodles seen from above" style="background:linear-gradient(135deg,#d9d2c4,#a89a82 50%,#5d5344)"></div>
  <div class="card-body">
    <h3 class="card-name">Udon Ya <span class="rating">5/10 Ratings</span></h3>
    <p class="card-desc">The Japanese ethos of devoting a restaurant to one dish or ingredient is admirable, yet rarely seen in this city. The fact that Soho would become home to a highly authentic one.</p>
    <div class="meta meta-price"><span class="disc"><svg class="ico"><use href="#i-tag"/></svg></span>Main courses £13-£37</div>
    <div class="meta meta-place"><span class="disc"><svg class="ico"><use href="#i-pin"/></svg></span>41 Copper Lane,<br>W1T 4ZZ</div>
    <div class="card-foot"><span class="phone"><svg class="ico"><use href="#i-phone"/></svg>020 7946 0123</span><span class="link"><svg class="ico"><use href="#i-link"/></svg>www.brasseriemarlow.co.uk</span></div>
  </div>
</article>

<article class="abs card" style="top:1878px">
  <div class="card-photo" role="img" aria-label="Robata grilled dish with smoke on a dark table" style="background:linear-gradient(135deg,#2c241f,#6e5a48 50%,#b7a592)"></div>
  <div class="card-body">
    <h3 class="card-name">Hibana <span class="rating">5/10 Ratings</span></h3>
    <p class="card-desc">This little sister has no trouble standing up for itself. The glass-fronted façade gives passers-by a peek of the chefs at work preparing robata-grilled goodies.</p>
    <div class="meta meta-price"><span class="disc"><svg class="ico"><use href="#i-tag"/></svg></span>Main courses £13-£37</div>
    <div class="meta meta-place"><span class="disc"><svg class="ico"><use href="#i-pin"/></svg></span>27 Linden Street,<br>W1T 6PP</div>
    <div class="card-foot"><span class="phone"><svg class="ico"><use href="#i-phone"/></svg>020 7946 0123</span><span class="link"><svg class="ico"><use href="#i-link"/></svg>www.brasseriemarlow.co.uk</span></div>
  </div>
</article>

<nav class="abs pager"><span class="arrow prev"></span><span>1</span><span>2</span><span class="current">3</span><span>4</span><span>5</span><span>6</span><span>7</span><span>8</span><span>9</span><span>.......</span><span>103</span><span>104</span><span>105</span><span>106</span><span class="arrow next"></span></nav>

<aside class="abs signup">
  <h3>Sign Up Now</h3>
  <p>Lorem Ipsum is simply dummy text of the printing and typesetting industry.</p>
  <span class="btn-green">SIGN UP</span>
  <div class="signup-figure" role="img" aria-label="Illustrated excited food fan pointing at the sign up button"></div>
</aside>

<section class="abs widget" style="top:656px;height:442px">
  <h4><svg><use href="#i-tag"/></svg>CATEGORIES</h4>
  <ul>
    <li>British Restaurants ( 10 )</li><li>French Restaurants ( 7 )</li><li>African Restaurants ( 13 )</li><li>Indian Restaurants ( 11 )</li><li>Italian Restaurants ( 6 )</li><li>Mexican Restaurants ( 2 )</li><li>British Restaurants ( 10 )</li><li>French Restaurants ( 7 )</li><li>African Restaurants ( 13 )</li><li>Emberline Air Street ( 11 )</li><li>Italian Restaurants ( 6 )</li><li>The Copper Pantry ( 2 )</li><li>British Restaurants ( 10 )</li><li>Larkspur Place ( 7 )</li>
  </ul>
</section>

<section class="abs widget" style="top:1114px;height:290px">
  <h4><svg><use href="#i-pin"/></svg>LOCATION</h4>
  <ul>
    <li>Restaurants in West London ( 3 )</li><li>Restaurants in East London ( 7 )</li><li>Restaurants in South America ( 3 )</li><li>Restaurants in Canada ( 10 )</li><li>Restaurants in New York ( 10 )</li><li>Mexican Restaurants ( 5 )</li><li>Restaurants in West London ( 3 )</li><li>Restaurants in East London ( 7 )</li><li>Restaurants in South America ( 3 )</li>
  </ul>
</section>

<section class="abs widget" style="top:1423px;height:130px">
  <h4><svg><use href="#i-tag"/></svg>PRICES</h4>
  <ul>
    <li>Casual Restaurants (€10 - €20) ( 0 )</li><li>Casual Restaurants (€10 - €20) ( 0 )</li><li>Casual Restaurants (€10 - €20) ( 0 )</li>
  </ul>
</section>

<section class="abs feature">
  <h4>Restaurant of the week</h4>
  <div class="feature-photo" role="img" aria-label="Elegant dining room with set tables and dark chairs"></div>
  <p>Solenne screamed of taste and class. Glass windows with flowing water looked amazing. Solenne brings to you a team of cooking professionals who are on the mission of pres ...</p>
  <div class="btns"><span style="width:74px">READ MORE</span><span style="width:100px">BOOK NOW</span></div>
</section>

<section class="abs tweets">
  <h5>Latest Tweets</h5>
  <small>Folow us on Chirpline</small>
  <span class="brace">}</span>
  <blockquote>Tickle your taste buds with a delicious and<br>mouth-watering dessert chirpline.com/tablehop</blockquote>
  <span class="bird"></span>
</section>

<footer class="abs footer">
  <div class="col col-latest">
    <h6>Latest Restaurants</h6>
    <div class="names"><span>Corner Tavern</span><span>Marco Delfino</span><span>Santa Lucia</span><span>Common Eating House</span><span>Il Pettirosso</span><span>Forno Rosso</span><span>Gelatiera</span><span>Hartley Arms</span></div>
  </div>
  <div class="col col-contact">
    <h6>Contact</h6>
    <div class="contact-row"><span class="disc"><svg class="ico"><use href="#i-mail"/></svg></span>info@tablehop.co.uk</div>
    <div class="contact-row"><span class="disc"><svg class="ico"><use href="#i-phone"/></svg></span>+1 (555) 010-4477</div>
  </div>
  <div class="col col-social">
    <h6>Connect with us</h6>
    <div class="social-row"><i></i>Friendwall</div>
    <div class="social-row"><i></i>Chirpline</div>
    <div class="social-row"><i></i>Linkwork</div>
    <div class="social-row"><i></i>Circleplus</div>
  </div>
  <div class="col col-news">
    <h6>Subscribe Newsletter</h6>
    <div class="news-input">Email Address</div>
    <div class="news-row"><span class="news-btn">Subscribe Now</span><small>Free Subscribe our latest offers and Plans.</small></div>
  </div>
</footer>
<div class="abs base">© 2013 TableHop.co.uk. All rights reserved.</div>
</body>
</html>
```